Korvane Technologies - Business Card & Stationary
"Moving Forward"
Everyone, we are making our decision now. Thank you for your patience.
Wow, you guys are really doing a superb job. We really like a majority of the designs submitted thus far. There is no clear winner yet, so please keep them coming!
A couple things: bluecrest - We like where you are going with #38, #41, & #42. I like the back of the card ideas you have had so far. We like the backs of #41, & #42, but the back of #40 is just too dark.
dorvalstudio - Like #20, #21, & #33. Really like the Grey/Silver logo on the back too.
lumbrafox - #37 is one of our favorites!
We would like to see what some of you guys have in mind for stationary too!
Great job everyone! 1, 3, 5, 6 - we really like the front design, but would like the back side to be more subtle. 10 & 11 are both great. Would like the logo centered on the back of #10 like #7. I am not too keen on the solid green areas like #'s 8 & 9.
This is a project to include business cards and stationary!! I apologize if that wasn't clear.

```html
<!DOCTYPE html>
<html lang="en">
<head>
<meta charset="UTF-8">
<title>Korvane Technologies – Business Card</title>
<link href="https://fonts.googleapis.com/css2?family=Arimo:wght@400;700&display=swap" rel="stylesheet">
<style>
  :root {
    --backdrop: #ebe6de;
    --card-white: #ffffff;
    --ink-dark: #2b3a42;
    --ink-grey: #5d6a70;
    --brand-blue: #1f6fb5;
    --brand-green: #2e8a4a;
    --deep-green: #0f3f33;
    --mid-green: #2a7a5a;
    --soft-silver: #dfe3e6;
    --tag-light: #cfe3da;
  }
  * { margin: 0; padding: 0; box-sizing: border-box; }
  html, body { width: 1200px; height: 533px; overflow: hidden; }
  body {
    background: var(--backdrop);
    font-family: "Arimo", Arial, sans-serif;
    position: relative;
  }
  .card {
    position: absolute;
    top: 144px;
    width: 388px;
    height: 306px;
    border-radius: 14px;
    overflow: hidden;
    box-shadow: 0 3px 10px rgba(0,0,0,0.18);
  }
  .card-front { left: 199px; background: var(--card-white); }
  .card-back {
    left: 622px;
    background: radial-gradient(circle at 50% 42%, var(--mid-green) 0%, var(--deep-green) 75%);
  }

  .front-decoration {
    position: absolute;
    left: -70px;
    top: 70px;
    width: 200px;
    height: 200px;
    border-radius: 50%;
    background: radial-gradient(circle at 60% 40%, #ffffff 0%, var(--soft-silver) 70%);
  }

  .brand {
    position: absolute;
    left: 160px;
    top: 34px;
    display: flex;
    align-items: center;
    gap: 10px;
  }
  .brand-dot {
    width: 46px; height: 46px; border-radius: 50%;
    background: var(--brand-green);
  }
  .brand-name {
    color: var(--ink-dark);
    font-weight: 700;
    font-size: 24px;
    line-height: 0.95;
    letter-spacing: 0.5px;
  }
  .brand-name span { display: block; font-size: 17px; letter-spacing: 1px; }
  .brand-tagline {
    position: absolute;
    left: 218px;
    top: 88px;
    font-size: 9px;
    letter-spacing: 4px;
    color: var(--ink-grey);
  }

  .person-name {
    position: absolute;
    left: 160px;
    top: 116px;
    color: var(--brand-blue);
    font-weight: 700;
    font-size: 15px;
    letter-spacing: 0.5px;
  }
  .contact {
    position: absolute;
    left: 160px;
    top: 160px;
    font-size: 10px;
    line-height: 14px;
    color: var(--ink-grey);
    list-style: none;
  }
  .contact .gap { margin-top: 10px; }
  .contact b { color: var(--brand-green); font-weight: 700; margin-right: 4px; }

  .front-band {
    position: absolute;
    left: 0; right: 0;
    top: 272px;
    height: 4px;
    background: linear-gradient(90deg, var(--brand-blue), var(--brand-green));
  }
  .front-band-thin {
    position: absolute;
    left: 0; right: 0;
    top: 279px;
    height: 1px;
    background: var(--brand-blue);
    opacity: 0.6;
  }

  .back-mark {
    position: absolute;
    left: 159px;
    top: 76px;
    width: 70px; height: 70px;
    border-radius: 50%;
    background: var(--brand-green);
    box-shadow: 0 0 24px rgba(120,220,170,0.35);
  }
  .back-tagline {
    position: absolute;
    left: 0; right: 0;
    top: 196px;
    text-align: center;
    color: var(--tag-light);
    font-size: 15px;
    letter-spacing: 5px;
  }
</style>
</head>
<body>
  <section class="card card-front">
    <div class="front-decoration" role="img" aria-label="Soft silver brand watermark shape"></div>
    <div class="brand">
      <div class="brand-dot"></div>
      <div class="brand-name">KORVANE<span>TECHNOLOGIES</span></div>
    </div>
    <div class="brand-tagline">MOVING FORWARD</div>
    <div class="person-name">DANIEL KORVANE</div>
    <ul class="contact">
      <li>PO Box 642</li>
      <li>Marlow Springs, Ohio 45821</li>
      <li class="gap"><b>T</b>855-KORVANE (567-8263)</li>
      <li><b>E</b>dan.korvane@korvanetech.com</li>
      <li><b>W</b>korvanetech.com</li>
    </ul>
    <div class="front-band"></div>
    <div class="front-band-thin"></div>
  </section>

  <section class="card card-back">
    <div class="back-mark"></div>
    <div class="back-tagline">MOVING FORWARD</div>
  </section>
</body>
</html>
```